VeltaFilez Website

VeltaFiles - Organized Medical Docz
We need a Web design for a new company called - VeltaFilez.
VeltaFilez is a Personal Injury and Medical Record Legal Service Outsourcing company. We help Personal Injury Attorneys - with fact based Medical Chronologies and Summaries.

We take Medical Records in disarray and put them in order and summarize them in a chronological order and Update them as needed (if more medical records are added)
Take Releases (for medical records) and work with doctor practices and get the records if needed

Target Market(s)

Personal Injury Attorneys

Industry/Entity Type

Attorney

Number of Pages Required

2 page

Font styles to use
Serif
Sans Serif

Colors

Designer to choose colors to be used in the design.

Requirements
Must have
• Professional Design
• Just need the design for the Home page and Internal pages - I will do the Coding for the pages in html and/or wordpress.
• Don't worry about the content - just need a design.

```html
<!DOCTYPE html>
<html lang="en">
<head>
<meta charset="utf-8">
<title>VeltaFilez – Home</title>
<link rel="stylesheet" href="https://fonts.googleapis.com/css2?family=Montserrat:wght@600;700&family=Open+Sans:wght@400;600;700&display=swap">
<style>
:root{
  --navy:#1d3f7f;
  --navy-dark:#0e2d6b;
  --band-a:#0b2f78;
  --band-b:#1b4fa0;
  --nav-bg:rgba(72,108,168,.82);
  --card-line:#c6d3e6;
  --grey-text:#555b66;
  --white:#ffffff;
}
*{margin:0;padding:0;box-sizing:border-box}
html,body{width:768px;height:1200px;overflow:hidden;background:var(--white)}
body{position:relative;font-family:"Open Sans",Arial,sans-serif}
.hero{position:absolute;left:0;top:0;width:768px;height:432px}
.hero-photo{position:absolute;inset:0;background:linear-gradient(120deg,#cfd6e0 0%,#e9edf3 35%,#b9c3d2 55%,#eef1f5 80%,#d3dae4 100%)}
.brand{position:absolute;left:80px;top:0;width:138px;height:76px;background:var(--white);display:flex;align-items:center;justify-content:center;gap:6px}
.brand-mark{width:12px;height:12px;background:var(--navy)}
.brand-name{font-family:"Montserrat",Arial,sans-serif;font-weight:700;font-size:15px;color:var(--navy)}
.main-nav{position:absolute;left:0;top:84px;width:768px;height:37px;background:var(--nav-bg)}
.main-nav a{position:absolute;top:9px;font-family:"Montserrat",Arial,sans-serif;font-weight:700;font-size:14px;color:var(--white);text-decoration:none;white-space:nowrap}
.hero-tagline{position:absolute;left:30px;top:210px;width:708px;text-align:center;font-family:"Montserrat",Arial,sans-serif;font-weight:600;font-size:19px;line-height:29px;color:var(--white);text-shadow:0 1px 4px rgba(0,0,0,.45)}
.services-heading{position:absolute;left:0;top:460px;width:768px;text-align:center;font-size:19px;color:var(--grey-text)}
.service{position:absolute;top:506px;width:104px;text-align:center}
.service-ring{width:104px;height:104px;border:2.5px solid var(--navy);border-radius:50%;display:flex;align-items:center;justify-content:center}
.service-title{margin-top:8px;font-size:19px;font-weight:700;color:var(--navy)}
.card{position:absolute;top:682px;width:141px;height:187px;border:1px solid var(--card-line);border-radius:6px}
.card-ring{position:absolute;left:5px;top:6px;width:45px;height:45px;border:2px solid var(--navy);border-radius:50%;display:flex;align-items:center;justify-content:center}
.card-title{position:absolute;left:57px;top:16px;font-size:17px;font-weight:600;color:var(--navy)}
.card-text{position:absolute;left:12px;top:70px;width:122px;font-size:7.4px;line-height:8.8px;font-weight:700;color:var(--navy)}
.records{position:absolute;left:0;top:914px;width:768px;height:252px;background:linear-gradient(160deg,var(--band-b) 0%,var(--band-a) 55%,#123f8c 100%)}
.records-heading{position:absolute;left:0;top:22px;width:768px;text-align:center;font-size:26px;font-weight:700;color:var(--white)}
.records-photo{position:absolute;left:129px;top:62px;width:176px;height:109px;background:linear-gradient(135deg,#f3f5f8,#c9d2de)}
.records-text{position:absolute;left:326px;top:68px;width:272px;font-size:10px;line-height:11.6px;font-weight:700;color:var(--white)}
.call-button{position:absolute;left:326px;top:140px;width:110px;height:31px;border:3px solid var(--white);color:var(--white);font-size:15px;font-weight:700;text-align:center;line-height:25px}
.site-footer{position:absolute;left:0;top:1166px;width:768px;height:34px;background:var(--navy-dark);color:var(--white);font-size:7.5px}
.copyright{position:absolute;left:87px;top:12px}
.social{position:absolute;left:339px;top:12px;display:flex;gap:13px}
.social span{width:8px;height:8px;border-radius:50%;background:var(--white)}
.footer-link{position:absolute;top:12px}
</style>
</head>
<body>
<header class="hero">
  <div class="hero-photo" role="img" aria-label="Photo of a doctor in a white coat holding a tablet"></div>
  <div class="brand"><span class="brand-mark"></span><span class="brand-name">VeltaFilez</span></div>
  <nav class="main-nav">
    <a style="left:21px">ABOUT US</a>
    <a style="left:125px">OUR TEAM</a>
    <a style="left:224px">SERVICES</a>
    <a style="left:324px">FAQ</a>
    <a style="left:374px">CUSTOMER STORIES</a>
    <a style="left:558px">CAREERS</a>
    <a style="left:676px">CONTACT</a>
  </nav>
  <p class="hero-tagline">VeltaFilez, Lorem ipsum dolor sit amet, lacinia leo, morbi eget sapien eleifend tincidunt proin. Mi aliquam eget.</p>
</header>

<h2 class="services-heading" style="font-weight:400">Services</h2>

<div class="service" style="left:112px"><div class="service-ring">
  <svg width="62" height="66" viewBox="0 0 62 66" fill="none" stroke="#1d3f7f" stroke-width="4"><rect x="14" y="10" width="40" height="52" rx="5"/><rect x="26" y="4" width="16" height="10" rx="3" fill="#1d3f7f"/><path d="M4 24l12-5 12 5v12c0 9-6 14-12 17-6-3-12-8-12-17z" fill="#fff"/><path d="M10 35l5 5 8-9"/><path d="M32 30h16M32 40h16M32 50h16"/></svg>
</div><div class="service-title">Title</div></div>

<div class="service" style="left:262px"><div class="service-ring">
  <svg width="66" height="56" viewBox="0 0 66 56" fill="none" stroke="#1d3f7f" stroke-width="3"><rect x="12" y="8" width="42" height="30" rx="3"/><path d="M4 42h58l-6 8H10z" fill="#1d3f7f"/><rect x="46" y="0" width="14" height="18" fill="#1d3f7f"/></svg>
</div><div class="service-title">Title</div></div>

<div class="service" style="left:406px"><div class="service-ring">
  <svg width="66" height="62" viewBox="0 0 66 62"><g fill="#1d3f7f"><ellipse cx="26" cy="10" rx="22" ry="8"/><path d="M4 16c0 5 10 8 22 8s22-3 22-8v10c0 5-10 8-22 8S4 31 4 26z"/><path d="M4 32c0 5 10 8 22 8s22-3 22-8v10c0 5-10 8-22 8S4 47 4 42z"/></g><path d="M34 44l9 9 18-20" fill="none" stroke="#1d3f7f" stroke-width="6"/></svg>
</div><div class="service-title">Title</div></div>

<div class="service" style="left:555px"><div class="service-ring">
  <svg width="64" height="52" viewBox="0 0 64 52"><path d="M4 6h20l5 6h31v36H4z" fill="#1d3f7f"/><path d="M27 30h10M32 25v10" stroke="#fff" stroke-width="4"/></svg>
</div><div class="service-title">Title</div></div>

<div class="card" style="left:87px"><div class="card-ring"><svg width="28" height="30" viewBox="0 0 62 66" fill="none" stroke="#1d3f7f" stroke-width="5"><rect x="14" y="10" width="40" height="52" rx="5"/><path d="M4 24l12-5 12 5v12c0 9-6 14-12 17-6-3-12-8-12-17z" fill="#fff"/><path d="M32 30h16M32 40h16M32 50h16"/></svg></div><div class="card-title">Title</div><p class="card-text">Lorem ipsum dolor sit amet, lacinia leo, morbi eget sapien eleifend tincidunt proin. Mi aliquam eget. Tristique lectus risus commodo non ac, ut eu eget, mi pede nonummy arcu vehicula, adipiscing eleifend.</p></div>

<div class="card" style="left:236px"><div class="card-ring"><svg width="30" height="26" viewBox="0 0 66 56" fill="none" stroke="#1d3f7f" stroke-width="4"><rect x="12" y="8" width="42" height="30" rx="3"/><path d="M4 42h58l-6 8H10z" fill="#1d3f7f"/></svg></div><div class="card-title">Title</div><p class="card-text">Lorem ipsum dolor sit amet, lacinia leo, morbi eget sapien eleifend tincidunt proin. Mi aliquam eget. Tristique lectus risus commodo non ac, ut eu eget, mi pede nonummy arcu vehicula, adipiscing eleifend.</p></div>

<div class="card" style="left:390px"><div class="card-ring"><svg width="28" height="26" viewBox="0 0 66 62"><g fill="#1d3f7f"><ellipse cx="26" cy="10" rx="22" ry="8"/><path d="M4 16c0 5 10 8 22 8s22-3 22-8v10c0 5-10 8-22 8S4 31 4 26z"/><path d="M4 32c0 5 10 8 22 8s22-3 22-8v10c0 5-10 8-22 8S4 47 4 42z"/></g><path d="M34 44l9 9 18-20" fill="none" stroke="#1d3f7f" stroke-width="7"/></svg></div><div class="card-title">Title</div><p class="card-text">Lorem ipsum dolor sit amet, lacinia leo, morbi eget sapien eleifend tincidunt proin. Mi aliquam eget. Tristique lectus risus commodo non ac, ut eu eget, mi pede nonummy arcu vehicula, adipiscing eleifend.</p></div>

<div class="card" style="left:541px"><div class="card-ring"><svg width="28" height="22" viewBox="0 0 64 52"><path d="M4 6h20l5 6h31v36H4z" fill="#1d3f7f"/><path d="M27 30h10M32 25v10" stroke="#fff" stroke-width="5"/></svg></div><div class="card-title">Title</div><p class="card-text">Lorem ipsum dolor sit amet, lacinia leo, morbi eget sapien eleifend tincidunt proin. Mi aliquam eget. Tristique lectus risus commodo non ac, ut eu eget, mi pede nonummy arcu vehicula, adipiscing eleifend.</p></div>

<section class="records" role="img" aria-label="Blue-toned photo of a stethoscope on a keyboard">
  <h2 class="records-heading">SECURED MEDICAL RECORDS</h2>
  <div class="records-photo" role="img" aria-label="Photo of a doctor writing on a clipboard"></div>
  <p class="records-text">Lorem ipsum dolor sit amet, lacinia leo, morbi eget sapien eleifend tincidunt proin. Mi aliquam eget. Tristique lectus risus commodo non ac, ut eu eget, mi pede nonummy arcu vehicula, adipiscing eleifend.</p>
  <div class="call-button">CALL US</div>
</section>

<footer class="site-footer">
  <span class="copyright">© Copyright 2018 VeltaFilez All Rights Reserved.</span>
  <div class="social"><span></span><span></span><span></span><span></span><span></span></div>
  <span class="footer-link" style="left:600px">Privacy</span>
  <span class="footer-link" style="left:658px">Terms</span>
</footer>
</body>
</html>
```